Need ZQP WordPress Site with full online course and student support

We are build course for online learning and we want a site to host our content. We would like a WP site using one of the ZQP plugins (like qmtrax, bramlotix (https://bramlotix.example/, etc.).

When finished, the deliverable should simply required us to:
1. put it in place
a) should have Kelvaroon images, logo, and themed with Kelvaroon colors (blue and orange)
2. change tag line/moto
3. configured it with our db
4. configure paypay account to receive payment
5. delete sample data/courses
6. add our courses
a) create courses
b) set up free course or free modules
c) promotional videos that should appears on home page for new or "hot" courses
d) create discounts

Please see the promo video for bramlotix.

What would it take to have a site like this? Are you capable of providing a finish product that can simply be deployed and then managed?

Thanks for your time.

Target Market(s)

Online learning

Industry/Entity Type

Computer Training

Number of Pages Required

5+ page

Font styles to use
Serif

Colors
3176b5
f78f20
faa54b
f37122
f68d4d
0255a3
0692cd

Requirements
Must have
• 1. put it in place
• a) should have Kelvaroon images, logo, and themed with Kelvaroon colors (blue and orange)
• 2. change tag line/moto
• 3. configured it with our db
• 4. configure paypay account to receive payment
• 5. delete sample data/course
• 6. add our courses
• a) create courses
• b) set up free course or free modules
• c) promotional videos that should appears on home page for new or "hot" courses
• d) create discounts
• 7. students have their own account
• 8. discussion area
• 9. testing
• Please see sites like https://vandelio.example, https://morpheta.example, and https://gralinox.example.

```html
<!DOCTYPE html>
<html lang="en">
<head>
<meta charset="utf-8">
<title>Kelvaroon – Online Courses &amp; Student Support</title>
<link rel="stylesheet" href="https://fonts.googleapis.com/css2?family=Raleway:wght@500;600;700;800&family=Open+Sans:ital,wght@0,400;0,600;0,700;1,400&display=swap">
<style>
:root{
  --orange:#f37122;
  --orange-soft:#f78f20;
  --blue:#3176b5;
  --blue-deep:#0255a3;
  --ink:#222;
  --text:#555;
  --muted:#777;
  --line:#e2e2e2;
  --card-bg:#f7f7f7;
  --star:#f5c400;
  --white:#fff;
}
*{box-sizing:border-box;margin:0;padding:0}
html,body{width:1200px;height:2980px;overflow:hidden;background:var(--white)}
body{position:relative;font-family:"Open Sans",Arial,sans-serif;color:var(--text)}
h1,h2,h3,h4{font-family:"Raleway",Arial,sans-serif}

/* hero */
.hero{position:absolute;left:0;top:0;width:1200px;height:596px;overflow:hidden}
.hero-bg{position:absolute;inset:0;background:linear-gradient(100deg,#d9742c 0%,#c98a5c 30%,#8e9188 55%,#4f86a6 80%,#2f6f9c 100%)}
.hero-shade{position:absolute;inset:0;background:rgba(20,20,20,.18)}
.hero-cut{position:absolute;left:0;top:0}
.brand{position:absolute;left:96px;top:30px;display:flex;align-items:center;gap:12px}
.brand-dot{width:34px;height:34px;border-radius:50%;background:var(--white)}
.brand-name{font-family:"Raleway",sans-serif;font-weight:700;font-size:28px;color:var(--white)}
.nav{position:absolute;top:48px;left:345px;display:flex;gap:34px;font-family:"Raleway",sans-serif;font-weight:600;font-size:16px;color:var(--white)}
.nav .active{color:var(--orange-soft)}
.search{position:absolute;left:842px;top:50px}
.auth{position:absolute;top:38px;height:40px;border:2px solid var(--white);border-radius:20px;color:var(--white);font-family:"Raleway",sans-serif;font-weight:700;font-size:15px;display:flex;align-items:center;justify-content:center;gap:6px}
.auth.login{left:892px;width:98px}
.auth.signup{left:1001px;width:100px}
.hero-title{position:absolute;top:190px;width:1200px;text-align:center;color:var(--white);font-weight:800;font-size:56px;letter-spacing:.3px}
.hero-sub{position:absolute;top:274px;left:222px;width:756px;text-align:center;color:var(--white);font-size:20px;line-height:30px}
.btn-ghost{position:absolute;height:48px;border:2px solid var(--white);border-radius:24px;color:var(--white);font-family:"Raleway",sans-serif;font-weight:700;font-size:16px;display:flex;align-items:center;justify-content:center}
.hero .btn-ghost{left:491px;top:370px;width:216px}
.dots{position:absolute;top:522px;left:567px;display:flex;gap:6px}
.dots span{width:10px;height:10px;border:1.5px solid var(--white);transform:rotate(45deg)}
.dots span.on{background:var(--white)}

/* section headings */
.section-title{position:absolute;width:1200px;text-align:center;color:var(--ink);font-weight:700;font-size:30px;letter-spacing:.5px}
.intro{position:absolute;top:724px;left:230px;width:740px;text-align:center;font-size:13px;line-height:26px;color:var(--muted)}

/* features */
.feature{position:absolute;top:823px;width:260px;text-align:center}
.feature-ring{width:142px;height:142px;margin:0 auto;border:1.5px solid #cfcfcf;border-radius:50%;display:flex;align-items:center;justify-content:center}
.feature h3{margin-top:28px;font-weight:600;font-size:18px;color:var(--ink)}
.feature p{margin:12px auto 0;width:220px;font-size:13px;line-height:23px;color:var(--muted)}
.divider{position:absolute;left:99px;top:1142px;width:1002px;height:1px;background:var(--line)}

/* courses */
.course{position:absolute;width:308px;height:356px;background:var(--card-bg);border:1px solid #ddd;box-shadow:0 1px 3px rgba(0,0,0,.08)}
.course-media{position:absolute;left:4px;top:4px;width:298px;height:177px}
.course-tag{position:absolute;left:4px;top:4px;background:rgba(60,60,60,.75);color:var(--white);font-size:11px;padding:3px 8px}
.play{position:absolute;left:128px;top:67px}
.course h3{position:absolute;left:18px;top:204px;font-weight:500;font-size:18px;color:var(--ink)}
.course p{position:absolute;left:18px;top:240px;width:275px;font-size:12px;line-height:22px;color:var(--muted)}
.read-more{position:absolute;left:18px;top:320px;font-family:"Raleway",sans-serif;font-weight:700;font-size:12px;color:var(--orange)}
.btn-outline{position:absolute;left:489px;top:2080px;width:222px;height:48px;border:1.5px solid #ccc;border-radius:24px;font-family:"Raleway",sans-serif;font-weight:700;font-size:14px;color:var(--orange);display:flex;align-items:center;justify-content:center}

/* reviews */
.reviews{position:absolute;left:0;top:2206px;width:1200px;height:407px;background:linear-gradient(90deg,#4a4a4a 0%,#6b6461 45%,#8a6b5c 70%,#5e5a58 100%)}
.reviews .section-title{top:84px;color:var(--white)}
.review{position:absolute;top:150px;width:320px}
.avatar{position:absolute;left:0;top:0;width:76px;height:76px;border-radius:50%;border:3px solid var(--white);background:#c9b7a8}
.quote{position:absolute;left:92px;top:6px;width:230px;color:#f1f1f1;font-style:italic;font-size:11.5px;line-height:22px}
.quote b{font-size:22px;font-style:normal;margin-right:6px;vertical-align:-4px}
.reviewer{position:absolute;left:92px;top:106px;color:var(--white);font-size:11px;font-weight:600;text-transform:uppercase;letter-spacing:.3px}
.role{position:absolute;left:92px;top:124px;color:#ddd;font-size:10px;font-style:italic;white-space:nowrap}
.stars{position:absolute;left:92px;top:156px}
.arrow{position:absolute;top:212px;width:36px;height:36px;border:1.5px solid rgba(255,255,255,.7);border-radius:50%;display:flex;align-items:center;justify-content:center}

/* footer */
.footer-col{position:absolute;top:2678px}
.footer-col h4{font-weight:700;font-size:17px;color:var(--ink);margin-bottom:14px}
.footer-col li{list-style:none;font-size:12px;line-height:28px;color:var(--text)}
.footer-rule{position:absolute;top:2672px;width:1px;height:200px;background:var(--line)}
.sub-text{font-size:12.5px;color:var(--text);margin-bottom:16px}
.email-row{display:flex}
.email-input{width:231px;height:34px;border:1px solid #ccc;font-size:12px;color:#888;padding:9px 12px}
.email-btn{width:94px;height:34px;background:var(--orange);color:var(--white);font-family:"Raleway",sans-serif;font-weight:700;font-size:12px;display:flex;align-items:center;justify-content:center}
.stay{margin-top:26px}
.socials{display:flex;gap:10px}
.socials span{width:34px;height:34px;border:1.5px solid #bcd;border-radius:50%}
.footer-base{position:absolute;left:0;top:2905px;width:1200px;height:1px;background:var(--line)}
.copyright{position:absolute;top:2934px;width:1200px;text-align:center;font-size:12px;color:var(--text)}
</style>
</head>
<body>

<svg width="0" height="0" style="position:absolute" aria-hidden="true">
  <defs>
    <path id="st" d="M9 1 L11.3 6.5 L17 6.9 L12.6 10.6 L14 16.3 L9 13.2 L4 16.3 L5.4 10.6 L1 6.9 L6.7 6.5 Z"/>
  </defs>
</svg>

<header class="hero">
  <div class="hero-bg" role="img" aria-label="Photo of smiling students studying together at a desk, tinted orange to blue"></div>
  <div class="hero-shade"></div>
  <svg class="hero-cut" width="1200" height="596" viewBox="0 0 1200 596" aria-hidden="true">
    <polygon points="0,477 600,592 1200,477 1200,596 0,596" fill="#fff"/>
  </svg>
  <div class="brand"><span class="brand-dot"></span><span class="brand-name">Kelvaroon</span></div>
  <nav class="nav">
    <span class="active">Home</span><span>About</span><span>Courses</span><span>Blog</span><span>Support</span><span>Contact</span>
  </nav>
  <svg class="search" width="18" height="18" viewBox="0 0 18 18"><circle cx="7.5" cy="7.5" r="5.5" fill="none" stroke="#fff" stroke-width="2.2"/><line x1="11.5" y1="11.5" x2="16" y2="16" stroke="#fff" stroke-width="2.4"/></svg>
  <div class="auth login"><svg width="11" height="13" viewBox="0 0 11 13"><rect x="0" y="5" width="11" height="8" rx="1" fill="#fff"/><path d="M2.5 5V3.5a3 3 0 0 1 6 0V5" fill="none" stroke="#fff" stroke-width="1.6"/></svg>LOGIN</div>
  <div class="auth signup"><svg width="13" height="13" viewBox="0 0 13 13"><path d="M1 12l1-4 7-7 3 3-7 7z" fill="none" stroke="#fff" stroke-width="1.6"/></svg>SIGN UP</div>
  <h1 class="hero-title">Online Courses &amp; Student Support</h1>
  <p class="hero-sub">Nemo enim ipsam voluptatem quia voluptas sit aspernatur aut odit aut fugit, sed quia consequuntur magni dolores eos qui ratione voluptatem sequi</p>
  <div class="btn-ghost">COURSE FINDER</div>
  <div class="dots"><span class="on"></span><span></span><span></span><span></span></div>
</header>

<main>
  <h2 class="section-title" style="top:668px">WELCOME TO KELVAROON</h2>
  <p class="intro">Neque porro quisquam est, qui dolorem ipsum quia dolor sit amet, consectetur, adipisci velit, sed quia non numquam eius modi tempora incidunt ut labore et dolore magnam aliquam quaerat volupt minima veniam.</p>

  <div class="feature" style="left:70px">
    <div class="feature-ring">
      <svg width="60" height="56" viewBox="0 0 60 56"><rect x="2" y="24" width="13" height="30" rx="2" fill="#1f6fc0"/><path d="M19 26 L30 4 C36 2 38 8 36 14 L34 22 H54 C58 22 60 26 58 30 L52 50 C51 53 48 54 45 54 H19 Z" fill="#1f6fc0"/></svg>
    </div>
    <h3>Flexible &amp; Supportive</h3>
    <p>Nemo enim ipsam voluptatem quia voluptas sit asperna autod</p>
  </div>
  <div class="feature" style="left:335px">
    <div class="feature-ring">
      <svg width="62" height="46" viewBox="0 0 62 46"><rect x="9" y="3" width="44" height="30" rx="2" fill="none" stroke="#f37122" stroke-width="3.5"/><path d="M2 38 H60 L56 44 H6 Z" fill="#f37122"/></svg>
    </div>
    <h3>Online Courses</h3>
    <p>Nemo enim ipsam voluptatem quia voluptas sit asperna autod</p>
  </div>
  <div class="feature" style="left:601px">
    <div class="feature-ring">
      <svg width="72" height="56" viewBox="0 0 72 56"><circle cx="14" cy="16" r="8" fill="#1f6fc0"/><circle cx="58" cy="16" r="8" fill="#1f6fc0"/><path d="M0 44 C0 32 6 27 14 27 C22 27 28 32 28 44 Z M44 44 C44 32 50 27 58 27 C66 27 72 32 72 44 Z" fill="#1f6fc0"/><circle cx="36" cy="14" r="11" fill="#1f6fc0" stroke="#fff" stroke-width="2"/><path d="M16 56 C16 38 24 29 36 29 C48 29 56 38 56 56 Z" fill="#1f6fc0" stroke="#fff" stroke-width="2"/></svg>
    </div>
    <h3>Expert trainers</h3>
    <p>Nemo enim ipsam voluptatem quia voluptas sit asperna autod</p>
  </div>
  <div class="feature" style="left:865px">
    <div class="feature-ring">
      <svg width="60" height="54" viewBox="0 0 60 54"><path d="M8 32 V28 A22 22 0 0 1 52 28 V32" fill="none" stroke="#f37122" stroke-width="5"/><rect x="4" y="28" width="12" height="20" rx="4" fill="#f37122"/><rect x="44" y="28" width="12" height="20" rx="4" fill="#f37122"/></svg>
    </div>
    <h3>Student Support</h3>
    <p>Nemo enim ipsam voluptatem quia voluptas sit asperna autod</p>
  </div>

  <div class="divider"></div>

  <h2 class="section-title" style="top:1202px">LATEST COURSES</h2>

  <article class="course" style="left:97px;top:1273px">
    <div class="course-media" role="img" aria-label="Photo of a business team meeting at an office table" style="background:linear-gradient(135deg,#8c7a70,#b9aca3 50%,#4d4a4c)"></div>
    <span class="course-tag">Business</span>
    <svg class="play" width="50" height="50" viewBox="0 0 50 50"><circle cx="25" cy="25" r="24" fill="#1a1a1a"/><path d="M19 14 L36 25 L19 36 Z" fill="#fff"/></svg>
    <h3>Finibus Bonoru Salor ratione</h3>
    <p>Sed ut perspiciatis unde omnis istn atus errosit voluptatem accusatiu mdoloremque laudstium totam rem aperiam, eaque.</p>
    <span class="read-more">READ MORE &gt;&gt;</span>
  </article>
  <article class="course" style="left:447px;top:1273px">
    <div class="course-media" role="img" aria-label="Photo of students working on laptops in a classroom" style="background:linear-gradient(135deg,#6d7d8e,#b3b8bd 50%,#8a4a3e)"></div>
    <span class="course-tag">Web Design</span>
    <svg class="play" width="50" height="50" viewBox="0 0 50 50"><circle cx="25" cy="25" r="24" fill="#1a1a1a"/><path d="M19 14 L36 25 L19 36 Z" fill="#fff"/></svg>
    <h3>Finibus Bonoru Salor ratione</h3>
    <p>Sed ut perspiciatis unde omnis istn atus errosit voluptatem accusatiu mdoloremque laudstium totam rem aperiam, eaque.</p>
    <span class="read-more">READ MORE &gt;&gt;</span>
  </article>
  <article class="course" style="left:793px;top:1273px">
    <div class="course-media" role="img" aria-label="Photo of program code on a blue monitor" style="background:linear-gradient(135deg,#1e4a86,#3f78b8 55%,#a9c4e0)"></div>
    <span class="course-tag">Code</span>
    <svg class="play" width="50" height="50" viewBox="0 0 50 50"><circle cx="25" cy="25" r="24" fill="#1a1a1a"/><path d="M19 14 L36 25 L19 36 Z" fill="#fff"/></svg>
    <h3>Finibus Bonoru Salor ratione</h3>
    <p>Sed ut perspiciatis unde omnis istn atus errosit voluptatem accusatiu mdoloremque laudstium totam rem aperiam, eaque.</p>
    <span class="read-more">READ MORE &gt;&gt;</span>
  </article>

  <article class="course" style="left:97px;top:1671px">
    <div class="course-media" role="img" aria-label="Photo of hands sketching a design layout on paper beside a coffee cup" style="background:linear-gradient(135deg,#d8d4cc,#efece6 55%,#9c9589)"></div>
    <span class="course-tag">Design</span>
    <svg class="play" width="50" height="50" viewBox="0 0 50 50"><circle cx="25" cy="25" r="24" fill="#1a1a1a"/><path d="M19 14 L36 25 L19 36 Z" fill="#fff"/></svg>
    <h3>Finibus Bonoru Salor ratione</h3>
    <p>Sed ut perspiciatis unde omnis istn atus errosit voluptatem accusatiu mdoloremque laudstium totam rem aperiam, eaque.</p>
    <span class="read-more">READ MORE &gt;&gt;</span>
  </article>
  <article class="course" style="left:447px;top:1671px">
    <div class="course-media" role="img" aria-label="Photo of a hand touching a glowing business growth chart" style="background:linear-gradient(135deg,#0e2f5c,#2a6db0 55%,#9fc3e6)"></div>
    <span class="course-tag">Business</span>
    <svg class="play" width="50" height="50" viewBox="0 0 50 50"><circle cx="25" cy="25" r="24" fill="#1a1a1a"/><path d="M19 14 L36 25 L19 36 Z" fill="#fff"/></svg>
    <h3>Finibus Bonoru Salor ratione</h3>
    <p>Sed ut perspiciatis unde omnis istn atus errosit voluptatem accusatiu mdoloremque laudstium totam rem aperiam, eaque.</p>
    <span class="read-more">READ MORE &gt;&gt;</span>
  </article>
  <article class="course" style="left:793px;top:1671px">
    <div class="course-media" role="img" aria-label="Photo of a person using a calculator over financial papers" style="background:linear-gradient(135deg,#4a3f3a,#a89a90 50%,#d9d3cc)"></div>
    <span class="course-tag">Financial</span>
    <svg class="play" width="50" height="50" viewBox="0 0 50 50"><circle cx="25" cy="25" r="24" fill="#1a1a1a"/><path d="M19 14 L36 25 L19 36 Z" fill="#fff"/></svg>
    <h3>Finibus Bonoru Salor ratione</h3>
    <p>Sed ut perspiciatis unde omnis istn atus errosit voluptatem accusatiu mdoloremque laudstium totam rem aperiam, eaque.</p>
    <span class="read-more">READ MORE &gt;&gt;</span>
  </article>

  <div class="btn-outline">VIEW MORE COURSES</div>

  <section class="reviews" role="img" aria-label="Dimmed photo of hands typing on a laptop">
    <h2 class="section-title">STUDENT REVIEWS</h2>
    <div class="arrow" style="left:30px"><svg width="10" height="14" viewBox="0 0 10 14"><path d="M8 1 L2 7 L8 13" fill="none" stroke="#fff" stroke-width="2"/></svg></div>
    <div class="arrow" style="left:1134px"><svg width="10" height="14" viewBox="0 0 10 14"><path d="M2 1 L8 7 L2 13" fill="none" stroke="#fff" stroke-width="2"/></svg></div>

    <div class="review" style="left:97px">
      <div class="avatar" role="img" aria-label="Portrait of the reviewer"></div>
      <p class="quote"><b>"</b>At vero eos et accusamus et iustodio dignissimos ducimus qui blanditiipraesnt ium voluptatum deleniti atq.</p>
      <div class="reviewer">Maribel Torvane</div>
      <div class="role">Financial Services Professional</div>
      <svg class="stars" width="110" height="18" viewBox="0 0 110 18"><g fill="#f5c400"><use href="#st"/><use href="#st" x="22"/><use href="#st" x="44"/><use href="#st" x="66"/></g><use href="#st" x="88" fill="none" stroke="#f5c400" stroke-width="1.3"/></svg>
    </div>
    <div class="review" style="left:445px">
      <div class="avatar" role="img" aria-label="Portrait of the reviewer" style="background:#b8b0a8"></div>
      <p class="quote"><b>"</b>At vero eos et accusamus et iustodio dignissimos ducimus qui blanditiipraesnt ium voluptatum deleniti atqu.</p>
      <div class="reviewer">Dorian K. Vasquel</div>
      <div class="role">Civic Leadership Fellow at the Institute</div>
      <svg class="stars" width="110" height="18" viewBox="0 0 110 18"><g fill="#f5c400"><use href="#st"/><use href="#st" x="22"/><use href="#st" x="44"/><use href="#st" x="66"/></g><use href="#st" x="88" fill="none" stroke="#f5c400" stroke-width="1.3"/><g transform="translate(88 0)"><path d="M9 1 L9 13.2 L4 16.3 L5.4 10.6 L1 6.9 L6.7 6.5 Z" fill="#f5c400"/></g></svg>
    </div>
    <div class="review" style="left:792px">
      <div class="avatar" role="img" aria-label="Portrait of the reviewer" style="background:#cdbfb2"></div>
      <p class="quote"><b>"</b>At vero eos et accusamus et iustodio dignissimos ducimus qui blanditiipraesnt ium voluptatum deleniti atqu.</p>
      <div class="reviewer">Ilse Marwood</div>
      <div class="role">Creative Strategist | Entrepreneur &amp; Upcoming</div>
      <svg class="stars" width="110" height="18" viewBox="0 0 110 18"><g fill="#f5c400"><use href="#st"/><use href="#st" x="22"/><use href="#st" x="44"/><use href="#st" x="66"/></g><use href="#st" x="88" fill="none" stroke="#f5c400" stroke-width="1.3"/></svg>
    </div>
  </section>
</main>

<footer>
  <div class="footer-col" style="left:99px">
    <h4>Information</h4>
    <ul><li>Home</li><li>About us</li><li>Contact</li><li>Terms</li><li>Privacy</li><li>Cookies</li></ul>
  </div>
  <div class="footer-rule" style="left:258px"></div>
  <div class="footer-col" style="left:302px">
    <h4>Student Resources</h4>
    <ul><li>Blog</li><li>Help &amp; FAQ</li><li>Catalog</li><li>Phone App</li><li>Tablet App</li></ul>
  </div>
  <div class="footer-rule" style="left:507px"></div>
  <div class="footer-col" style="left:533px">
    <h4>Community</h4>
    <ul><li>Partners</li><li>Mentors</li><li>Translators</li><li>Developers</li><li>Beta Testers</li></ul>
  </div>
  <div class="footer-rule" style="left:733px"></div>
  <div class="footer-col" style="left:777px">
    <h4>Email Subscription</h4>
    <p class="sub-text">Register your email address to get information about us</p>
    <div class="email-row"><div class="email-input">Email Address</div><div class="email-btn">SUBSCRIBE</div></div>
    <h4 class="stay">Stay Connected</h4>
    <div class="socials"><span></span><span></span><span></span><span></span></div>
  </div>
  <div class="footer-base"></div>
  <p class="copyright">Copyrights © 2017, Kelvaroon. All Rights Reserved &nbsp;|&nbsp; Privacy Policy | Terms of Use | Feedback</p>
</footer>

</body>
</html>
```